Website for new dental office

I am Dr. Calvin Merrow and am building a new dental practice. I specialize in general dentistry. I am young and have a higher end dental practice incorporating very new technologies and would like my website to reflect that. As many dental patients are older, the website must be very easy to navigate. I would like patients to be able to request appointments, and will eventually add on patient information forms (the health history, etc, that you normally fill out in the practice) from my practice management software, so leave an area for that.

Industry/Entity Type

Building

```html
<!DOCTYPE html>
<html lang="en">
<head>
<meta charset="utf-8">
<title>Calvin Merrow, DDS — General Dentistry</title>
<link href="https://fonts.googleapis.com/css2?family=Open+Sans:wght@300;400;600;700&family=Noto+Serif:wght@400;700&family=Cinzel:wght@400;500&display=swap" rel="stylesheet">
<style>
:root{
  --blue:#3f5aa6;
  --blue-soft:#5570b8;
  --ink:#333333;
  --muted:#8f8f8f;
  --green:#7cc314;
  --orange:#f39320;
  --panel:#f2f2f2;
  --footer:#2c2c2c;
  --footer-base:#1d1d1d;
  --line:#dcdcdc;
}
*{box-sizing:border-box;margin:0;padding:0}
html,body{width:1200px;height:2163px;overflow:hidden}
body{position:relative;background:#fff;font-family:"Open Sans",sans-serif;color:var(--ink)}
.abs{position:absolute}

/* header */
.top-rule{left:0;top:0;width:1200px;height:7px;background:var(--blue)}
.brand{left:111px;top:52px;font-family:"Cinzel",serif;font-size:40px;font-weight:500;color:#2a2a2a;letter-spacing:.5px}
.brand span{color:var(--blue)}
.callout{right:158px;top:52px;text-align:right}
.callout .call{font-size:23px;color:#555;font-weight:300}
.callout .call b{font-weight:400;color:#333}
.callout .note{font-size:17px;color:var(--blue);margin-top:2px}
.phone-badge{left:1052px;top:52px;width:38px;height:38px}

/* nav */
.nav{left:0;top:144px;width:1200px;height:54px;border-top:3px solid var(--blue);border-bottom:3px solid var(--blue)}
.nav ul{list-style:none;display:flex;align-items:center;position:absolute;left:111px;top:0;height:48px;width:979px;justify-content:space-between}
.nav li{font-size:15px;color:#333}
.nav li.active{background:var(--blue);color:#fff;font-weight:700;width:121px;height:51px;margin-top:-1px;display:flex;align-items:center;justify-content:center;font-size:15px}
.nav li:last-child{margin-right:18px}

/* hero */
.hero{left:0;top:199px;width:1200px;height:537px;background:linear-gradient(90deg,#d5e0ea 0%,#e4ecf2 35%,#cbd9e5 60%,#e9eff3 85%,#dfe7ee 100%)}
.hero-title{left:111px;top:382px;font-size:36px;font-weight:400;color:#333}
.hero-title strong{color:var(--blue);font-weight:600}
.hero-copy{left:114px;top:443px;width:520px;font-size:13px;line-height:20px;color:#333}
.btn-free{left:112px;top:529px;width:218px;height:46px;background:var(--green);color:#fff;font-size:23px;display:flex;align-items:center;justify-content:center;border-radius:2px;font-weight:300}
.btn-free b{font-weight:700;margin-right:6px}

/* appointment */
.appointment{left:111px;top:738px;width:979px;height:110px;background:linear-gradient(#f6f6f6,#e6e6e6);box-shadow:0 10px 16px -10px rgba(0,0,0,.25)}
.appointment h2{position:absolute;left:17px;top:24px;font-size:25px;font-weight:300;line-height:31px;color:#333}
.appointment h2 b{font-weight:600}
.field{position:absolute;width:291px;height:29px;background:#fff;border:1px solid #d8d8d8;font-size:11px;color:#666;padding:6px 9px}
.btn-submit{position:absolute;left:822px;top:34px;width:140px;height:46px;background:linear-gradient(#fba43a,var(--orange));color:#fff;font-weight:700;font-size:23px;display:flex;align-items:center;justify-content:center;border-radius:2px;letter-spacing:.5px}

/* welcome */
.welcome-photo{left:87px;top:865px;width:533px;height:267px;background:linear-gradient(90deg,#e9eef3 0%,#cfd9e3 25%,#c3a58c 55%,#7d96b3 80%,#dfe4ea 100%)}
.welcome-title{left:114px;top:1165px;font-size:27px;font-weight:300;color:#333}
.welcome-title b{font-weight:400}
.welcome-copy{left:115px;top:1205px;width:565px;font-size:12.5px;line-height:18px;color:#a5a5a5}
.btn-dark{left:112px;top:1354px;width:112px;height:36px;background:#2f2f2f;color:#fff;font-size:14px;display:flex;align-items:center;justify-content:center}

/* case studies */
.case-title{left:725px;top:886px;font-size:22px;font-weight:400;color:#333}
.case-panel{left:725px;top:923px;width:354px;height:479px;background:var(--panel);border-top:3px solid #e4e4e4}
.case{position:absolute;left:21px;width:320px}
.case-img{position:absolute;left:0;top:0;width:144px;height:94px;border:1px solid #ddd}
.case h3{position:absolute;left:155px;top:2px;font-size:16px;font-weight:400;color:#333;white-space:nowrap}
.case p{position:absolute;left:157px;top:26px;width:160px;font-size:11px;line-height:16px;color:#aaa}
.case .more{position:absolute;left:157px;top:63px;width:77px;height:24px;background:var(--blue-soft);color:#fff;font-size:12px;display:flex;align-items:center;justify-content:center}

.divider{left:111px;top:1427px;width:979px;height:2px;background:#ececec}

/* section headings */
.sec-head{font-size:22px;font-weight:400;color:#222;display:flex;align-items:center;white-space:nowrap}
.sec-head .bar{display:inline-block;height:4px;background:var(--blue);margin-left:10px}
.sec-head .dots{display:inline-block;height:0;border-top:2px dotted #cfcfcf;margin-top:2px}

.stories-head{left:114px;top:1457px}
.stories-copy{left:115px;top:1498px;width:585px;font-size:12.5px;line-height:18px;color:#444}
.checks{left:112px;top:1577px;list-style:none}
.checks li{display:flex;align-items:center;height:35.5px;font-size:14px;color:#444}
.checks svg{width:28px;height:28px;margin-right:10px}
.btn-orange{left:111px;top:1774px;width:108px;height:32px;background:var(--orange);color:#fff;font-size:13px;display:flex;align-items:center;justify-content:center}

.testi-head{left:756px;top:1457px}
.testi-photo{left:757px;top:1497px;width:315px;height:180px;background:linear-gradient(135deg,#f4efeb 0%,#e0c2ad 45%,#d4a98f 60%,#f2ece7 100%);border:1px solid #e2e2e2}
.quote-badge{left:886px;top:1652px;width:50px;height:50px}
.testi-quote{left:782px;top:1708px;width:265px;text-align:center;font-size:15px;line-height:25px;color:#333;font-family:"Noto Serif",serif;font-weight:400;letter-spacing:.3px}
.testi-name{left:757px;top:1790px;width:315px;text-align:center;font-size:11px;color:#888}
.testi-name span{color:var(--blue)}

/* footer */
.footer{left:0;top:1836px;width:1200px;height:284px;background:var(--footer)}
.foot-brand{left:112px;top:1876px;font-family:"Noto Serif",serif;font-size:30px;color:#fff;font-weight:400;white-space:nowrap}
.foot-brand b{font-weight:700}
.foot-about{left:115px;top:1938px;width:265px;font-size:12.5px;line-height:18px;color:#e6e6e6}
.social{left:117px;top:2050px;display:flex;gap:5px}
.social i{display:block;width:24px;height:24px;border-radius:50%;background:#555}
.foot-col h4{font-size:18px;font-weight:400;color:#fff;margin-bottom:24px}
.foot-nav{left:446px;top:1868px}
.foot-nav ul{list-style:none;font-size:13px;line-height:18px;color:#fff}
.foot-contact{left:627px;top:1868px}
.foot-contact p{font-size:13px;line-height:20px;color:#fff;display:flex;align-items:center}
.foot-contact svg{width:12px;height:12px;margin-right:8px}
.foot-contact h4{margin-bottom:14px}
.foot-find{left:860px;top:1870px}
.map{left:860px;top:1911px;width:227px;height:166px;background:linear-gradient(135deg,#eef0ec,#dde2dc 50%,#e9e6dc);border:3px solid #fff}
.base{left:0;top:2120px;width:1200px;height:43px;background:var(--footer-base);color:#fff;font-size:12.5px;display:flex;align-items:center;justify-content:center}
</style>
</head>
<body>

<div class="abs top-rule"></div>

<header>
  <div class="abs brand">Calvin Merrow, <span>DDS</span></div>
  <div class="abs callout">
    <div class="call">Call: <b>+100 555 0147</b></div>
    <div class="note">For Free Consultancy We are here for You 24/7</div>
  </div>
  <svg class="abs phone-badge" viewBox="0 0 38 38" aria-hidden="true">
    <path d="M9 6c-3 2-4 6-2 10 3 7 8 12 15 15 4 2 7 0 9-2l-4-5-4 2c-4-2-7-5-9-9l2-4z" fill="none" stroke="#555" stroke-width="2.4"/>
    <circle cx="27" cy="12" r="9" fill="#fff" stroke="var(--blue)" stroke-width="2"/>
    <text x="27" y="16" font-size="10" text-anchor="middle" fill="var(--blue)" font-family="Open Sans,sans-serif" font-weight="700">24</text>
  </svg>
</header>

<nav class="abs nav">
  <ul>
    <li class="active">HOME</li>
    <li>Our Team</li>
    <li>Philosophy</li>
    <li>Restorative</li>
    <li>Cosmetic</li>
    <li>Tooth Replacement</li>
    <li>First Visit</li>
    <li>Contact</li>
  </ul>
</nav>

<section>
  <div class="abs hero" role="img" aria-label="Smiling dentist in a white coat with stethoscope, seated at a desk in a bright clinic"></div>
  <h1 class="abs hero-title">I Specialize In <strong>General Dentistry</strong></h1>
  <p class="abs hero-copy">Lorem Ipsum is simply dummy text of the printing and typesetting industry.<br>Lorem Ipsum has been the industry's standard dummy text ever since the 1500s,<br>when an unknown printer took a galley of type.</p>
  <div class="abs btn-free"><b>FREE</b> Consultancy</div>
</section>

<section class="abs appointment">
  <h2>Request an<br><b>Appointment</b></h2>
  <div class="field" style="left:209px;top:22px">Name</div>
  <div class="field" style="left:516px;top:22px">Email Address</div>
  <div class="field" style="left:209px;top:65px">Phone Number</div>
  <div class="field" style="left:516px;top:65px">Preferred Day</div>
  <div class="btn-submit">SUBMIT</div>
</section>

<section>
  <div class="abs welcome-photo" role="img" aria-label="Dentist holding a clipboard beside a smiling patient in the dental chair"></div>
  <h2 class="abs welcome-title">Welcome to <b>Calvin Merrow,DDS</b></h2>
  <p class="abs welcome-copy">Lorem Ipsum is simply dummy text of the printing and typesetting industry. Lorem Ipsum has been the industry's standard dummy text ever since the 1500s, when an unknown printer took a galley of type and scrambled it to make a type specimen book. It has survived not only five centuries, but also the leap into electronic typesetting, remaining essentially unchanged. It was popularised in the 1960s with the release of Typefold sheets containing Lorem Ipsum passages, and more recently with desktop publishing software like Quillset Pages including versions of Lorem Ipsum.</p>
  <div class="abs btn-dark">Read More</div>
</section>

<aside>
  <h2 class="abs case-title">Case Studies</h2>
  <div class="abs case-panel">
    <div class="case" style="top:19px">
      <div class="case-img" role="img" aria-label="Close-up of teeth with a dental mirror" style="background:linear-gradient(135deg,#c9434b,#f1e7e3 55%,#5a8fc7)"></div>
      <h3>Preventive</h3>
      <p>Lorem ipsum dolor sit amet, consectetur adipisicing elit,</p>
      <div class="more">Read More</div>
    </div>
    <div class="case" style="top:135px">
      <div class="case-img" role="img" aria-label="Close-up of a smile with dental floss" style="background:linear-gradient(135deg,#f4eeea,#cf7b78 50%,#f2e9e5)"></div>
      <h3>Restorative</h3>
      <p>Lorem ipsum dolor sit amet, consectetur adipisicing elit,</p>
      <div class="more">Read More</div>
    </div>
    <div class="case" style="top:251px">
      <div class="case-img" role="img" aria-label="Close-up of a bright white smile" style="background:linear-gradient(135deg,#e8c6b2,#d49a86 50%,#f1dacd)"></div>
      <h3>Cosmetic Dentistry</h3>
      <p>Lorem ipsum dolor sit amet, consectetur adipisicing elit,</p>
      <div class="more">Read More</div>
    </div>
    <div class="case" style="top:368px">
      <div class="case-img" role="img" aria-label="Set of dentures on a white background" style="background:linear-gradient(135deg,#fafafa,#e6a18e 50%,#fafafa)"></div>
      <h3>Tooth Replacement</h3>
      <p>Lorem ipsum dolor sit amet, consectetur adipisicing elit,</p>
      <div class="more">Read More</div>
    </div>
  </div>
</aside>

<div class="abs divider"></div>

<section>
  <h2 class="abs sec-head stories-head">Patient Stories<span class="bar" style="width:94px"></span><span class="dots" style="width:336px"></span></h2>
  <p class="abs stories-copy">Lorem Ipsum is simply dummy text of the printing and typesetting industry. Lorem Ipsum has been the industry's standard dummy text ever since the 1500s, when an unknown printer took a galley of type and scrambled it to make a type specimen book.</p>
  <ul class="abs checks">
    <li><svg viewBox="0 0 28 28" aria-hidden="true"><circle cx="14" cy="14" r="14" fill="var(--blue)"/><path d="M8 14l4 4 8-9" fill="none" stroke="#fff" stroke-width="3"/></svg>Lorem ipsum dolor sit amet, consectetur adipisicing elit, sed do.</li>
    <li><svg viewBox="0 0 28 28" aria-hidden="true"><circle cx="14" cy="14" r="14" fill="var(--blue)"/><path d="M8 14l4 4 8-9" fill="none" stroke="#fff" stroke-width="3"/></svg>Lorem ipsum dolor sit amet, consectetur adipisicing elit, sed do.</li>
    <li><svg viewBox="0 0 28 28" aria-hidden="true"><circle cx="14" cy="14" r="14" fill="var(--blue)"/><path d="M8 14l4 4 8-9" fill="none" stroke="#fff" stroke-width="3"/></svg>Lorem ipsum dolor sit amet, consectetur adipisicing elit, sed do.</li>
    <li><svg viewBox="0 0 28 28" aria-hidden="true"><circle cx="14" cy="14" r="14" fill="var(--blue)"/><path d="M8 14l4 4 8-9" fill="none" stroke="#fff" stroke-width="3"/></svg>Lorem ipsum dolor sit amet, consectetur adipisicing elit, sed do.</li>
    <li><svg viewBox="0 0 28 28" aria-hidden="true"><circle cx="14" cy="14" r="14" fill="var(--blue)"/><path d="M8 14l4 4 8-9" fill="none" stroke="#fff" stroke-width="3"/></svg>Lorem ipsum dolor sit amet, consectetur adipisicing elit, sed do.</li>
  </ul>
  <div class="abs btn-orange">Read More</div>
</section>

<section>
  <h2 class="abs sec-head testi-head">Testimonials<span class="bar" style="width:56px"></span><span class="dots" style="width:147px"></span></h2>
  <div class="abs testi-photo" role="img" aria-label="Smiling woman resting her chin on her hands"></div>
  <svg class="abs quote-badge" viewBox="0 0 50 50" aria-hidden="true">
    <circle cx="25" cy="25" r="25" fill="var(--blue)"/>
    <path d="M14 30v-6c0-4 2-7 6-8v3c-2 1-3 2-3 4h3v7zM27 30v-6c0-4 2-7 6-8v3c-2 1-3 2-3 4h3v7z" fill="#fff"/>
  </svg>
  <p class="abs testi-quote">„ Praesent vestibulum molestie lacus. Aenean nonummy. Hendrerit mauris phasellus.”</p>
  <p class="abs testi-name">Nora Haldane, <span>29 years</span></p>
</section>

<footer>
  <div class="abs footer"></div>
  <div class="abs foot-brand">Calvin Merrow, <b>DDS</b></div>
  <p class="abs foot-about">Lorem ipsum dolor sit amet, consectetur adipisicing elit, sed do eiusmod tempor incididunt ut labore et dolore magna aliqua. Ut enim ad minim veniam, quis nostrud exercitation.</p>
  <div class="abs social" aria-hidden="true"><i></i><i></i><i></i><i></i><i></i><i></i><i></i></div>

  <div class="abs foot-col foot-nav">
    <h4>Navigation</h4>
    <ul>
      <li>Home</li><li>Our Team</li><li>Philosophy</li><li>Restorative</li><li>Cosmetic</li><li>Tooth Replacement</li><li>First Visit Contact</li>
    </ul>
  </div>

  <div class="abs foot-col foot-contact">
    <h4>Contact Us</h4>
    <p><svg viewBox="0 0 12 12" aria-hidden="true"><path d="M2 1c-1 1-1 3 0 5 1 2 3 4 5 5 2 1 3 0 4-1L9 8 7 9C5 8 4 7 3 5l1-2z" fill="#fff"/></svg>Phone : +100 555 0198</p>
    <p><svg viewBox="0 0 12 12" aria-hidden="true"><rect x="0" y="2" width="12" height="8" fill="#fff"/><path d="M0 2l6 5 6-5" fill="none" stroke="#2c2c2c" stroke-width="1.2"/></svg>Email &nbsp;: info@calvinmerrow.com</p>
  </div>

  <div class="abs foot-col foot-find"><h4>Find Us</h4></div>
  <div class="abs map" role="img" aria-label="Street map showing the practice location"></div>

  <div class="abs base">Copyright © 2014 Calvin Merrow . All Rights Reserved.</div>
</footer>

</body>
</html>
```